Flyer Needed for Westland Advocacy Summit 2017

We need a flyer designed for a save the date for Verdant Goods Forum in California on August 23, 2017. The lobby day is taking place in Sacramento so please design the flyer using these details.

Requirements
Must have
• - Date must be clear
Nice to have
• - Must have "save the date"
• - Something that catches your eye

```html
<!DOCTYPE html>
<html lang="en">
<head>
<meta charset="UTF-8">
<title>Verdant Goods Forum 2017 – Save the Date</title>
<link href="https://fonts.googleapis.com/css2?family=Great+Vibes&family=Montserrat:wght@400;600&display=swap" rel="stylesheet">
<style>
  :root {
    --stage: #2b2b2d;
    --sky-top: #3d2c88;
    --sky-mid: #8a5cae;
    --sky-glow: #d98a8e;
    --dusk: #e8925c;
    --city: #3a2440;
    --water: #3a2f5c;
    --lights: #ffb347;
    --lights-deep: #d9622b;
    --flag-red: #a8323e;
    --green-dark: #4f6b4a;
    --green-mid: #6c8a62;
    --green-light: #a3b896;
    --paper: #ffffff;
    --ink: #3a3a3a;
    --url: #d4ecbf;
    --ribbon: #b9484b;
    --ribbon-dark: #8e3034;
    --white: #ffffff;
  }
  * { margin: 0; padding: 0; box-sizing: border-box; }
  html, body { width: 1200px; height: 960px; overflow: hidden; }
  body { background: var(--stage); font-family: "Montserrat", sans-serif; }

  .flyer {
    position: absolute; left: 277px; top: 24px;
    width: 646px; height: 912px; overflow: hidden;
    background: var(--paper);
    box-shadow: 0 8px 24px rgba(0,0,0,.5);
  }
  .flyer-shapes { position: absolute; inset: 0; }

  .save-line {
    position: absolute; left: 42px; top: 62px;
    font-family: "Great Vibes", cursive; font-size: 32px;
    color: var(--white); line-height: 1;
  }
  .title {
    position: absolute; font-family: "Great Vibes", cursive; font-weight: 400;
    color: var(--white); line-height: 1;
    text-shadow: 2px 3px 4px rgba(40,20,60,.55);
  }
  .title-first { left: 132px; top: 92px; font-size: 80px; }
  .title-second { left: 196px; top: 160px; font-size: 80px; }

  .ribbon { position: absolute; left: 212px; top: 258px; width: 186px; height: 34px; }
  .ribbon-label {
    position: absolute; left: 212px; top: 258px; width: 186px; height: 28px;
    line-height: 28px; text-align: center;
    color: var(--white); font-size: 14px; font-weight: 400;
  }

  .web-address {
    position: absolute; left: 92px; top: 728px;
    color: var(--url); font-size: 20px; font-weight: 400;
  }
  .event-details {
    position: absolute; left: 36px; top: 842px;
    color: var(--ink); font-size: 18px; line-height: 23px;
  }
  .event-details sup { font-size: 10px; }

  .organizer {
    position: absolute; left: 392px; top: 846px;
    display: flex; align-items: center; gap: 10px;
  }
  .organizer-mark { width: 24px; height: 24px; background: var(--green-mid); }
  .organizer-name { color: var(--ink); font-size: 16px; font-weight: 600; }
</style>
</head>
<body>
  <main class="flyer">
    <svg class="flyer-shapes" viewBox="0 0 646 912" width="646" height="912">
      <defs>
        <linearGradient id="sky" x1="0" y1="0" x2="0" y2="1">
          <stop offset="0" stop-color="var(--sky-top)"/>
          <stop offset="0.25" stop-color="var(--sky-mid)"/>
          <stop offset="0.42" stop-color="var(--sky-glow)"/>
          <stop offset="0.52" stop-color="var(--dusk)"/>
          <stop offset="0.6" stop-color="var(--city)"/>
          <stop offset="0.75" stop-color="var(--water)"/>
          <stop offset="1" stop-color="var(--water)"/>
        </linearGradient>
        <radialGradient id="bridge-glow" cx="0.25" cy="0.78" r="0.55">
          <stop offset="0" stop-color="var(--lights)" stop-opacity="0.85"/>
          <stop offset="0.45" stop-color="var(--lights-deep)" stop-opacity="0.45"/>
          <stop offset="1" stop-color="var(--lights-deep)" stop-opacity="0"/>
        </radialGradient>
        <radialGradient id="skyline-glow" cx="0.78" cy="0.55" r="0.38">
          <stop offset="0" stop-color="var(--lights)" stop-opacity="0.55"/>
          <stop offset="1" stop-color="var(--lights)" stop-opacity="0"/>
        </radialGradient>
        <radialGradient id="water-tint" cx="0.8" cy="0.82" r="0.3">
          <stop offset="0" stop-color="var(--flag-red)" stop-opacity="0.5"/>
          <stop offset="1" stop-color="var(--flag-red)" stop-opacity="0"/>
        </radialGradient>
      </defs>
      <g class="cityscape-photo" role="img"
         aria-label="Photo of a lit suspension bridge and city skyline over the bay at dusk, with a faded flag over the water">
        <rect x="0" y="0" width="646" height="800" fill="url(#sky)"/>
        <rect x="0" y="0" width="646" height="800" fill="url(#bridge-glow)"/>
        <rect x="0" y="0" width="646" height="800" fill="url(#skyline-glow)"/>
        <rect x="0" y="0" width="646" height="800" fill="url(#water-tint)"/>
      </g>
      <polygon class="band-dark" points="0,638 422,720 646,752 646,800 0,768" fill="var(--green-dark)"/>
      <polygon class="band-mid" points="0,700 300,710 646,752 646,800 0,768" fill="var(--green-mid)" opacity="0.85"/>
      <polygon class="band-light" points="426,758 646,752 646,800" fill="var(--green-light)"/>
      <polygon class="paper" points="0,768 430,758 646,800 646,912 0,912" fill="var(--paper)"/>
    </svg>

    <p class="save-line">Save the date for</p>
    <h1 class="title title-first">Verdant</h1>
    <h1 class="title title-second">Goods</h1>

    <svg class="ribbon" viewBox="0 0 186 34" width="186" height="34" aria-hidden="true">
      <polygon points="0,8 24,8 24,34 0,34 8,21" fill="var(--ribbon-dark)"/>
      <polygon points="186,8 162,8 162,34 186,34 178,21" fill="var(--ribbon-dark)"/>
      <rect x="24" y="0" width="138" height="28" fill="var(--ribbon)"/>
    </svg>
    <p class="ribbon-label">FORUM 2017</p>

    <p class="web-address">www.verdantgoodsforum.org</p>

    <p class="event-details">Wednesday, August 23<sup>rd</sup> 2017<br>CALIFORNIA</p>

    <div class="organizer">
      <span class="organizer-mark"></span>
      <span class="organizer-name">Verdant Goods Alliance</span>
    </div>
  </main>
</body>
</html>
```